Oil and Gas Exploration and Production company needs a business card design

We need a business card design using our logo and colors in the logo. We want a mainstream design.

```html
<!DOCTYPE html>
<html lang="en">
<head>
<meta charset="utf-8">
<title>Solara Oil &amp; Gas — Business Card</title>
<link href="https://fonts.googleapis.com/css2?family=Libre+Baskerville:wght@700&family=Nunito+Sans:wght@400&display=swap" rel="stylesheet">
<style>
  :root {
    --page-bg: #ececec;
    --card-bg: #ffffff;
    --pattern-tone: #f3f3f3;
    --gold: #b8963a;
    --gold-light: #eadfa6;
    --ink: #111111;
    --on-gold: #ffffff;
  }
  html, body {
    margin: 0;
    width: 1200px;
    height: 830px;
    overflow: hidden;
    background: var(--page-bg);
  }
  .card {
    position: absolute;
    left: 100px;
    top: 135px;
    width: 1000px;
    height: 560px;
    background: var(--card-bg);
    box-shadow: 0 6px 18px rgba(0,0,0,0.12);
    overflow: hidden;
  }
  .card__pattern {
    position: absolute;
    inset: 0;
    background: radial-gradient(circle at 50% 45%, var(--pattern-tone), var(--card-bg) 75%);
  }
  .card__art {
    position: absolute;
    inset: 0;
  }
  .brand {
    position: absolute;
    left: 0;
    right: 0;
    top: 170px;
    display: flex;
    justify-content: center;
    align-items: center;
    gap: 18px;
  }
  .brand__dot {
    width: 38px;
    height: 38px;
    border-radius: 50%;
    background: var(--ink);
  }
  .brand__name {
    font-family: "Libre Baskerville", serif;
    font-weight: 700;
    font-size: 64px;
    color: var(--ink);
    letter-spacing: -0.5px;
  }
  .contact {
    position: absolute;
    left: 88px;
    top: 358px;
    margin: 0;
    padding: 0;
    list-style: none;
    font-family: "Nunito Sans", sans-serif;
    font-size: 31px;
    color: var(--ink);
  }
  .contact__item {
    display: flex;
    align-items: center;
    gap: 14px;
    height: 42px;
  }
  .contact__icon {
    width: 24px;
    height: 24px;
    flex: none;
  }
  .holder {
    position: absolute;
    left: 740px;
    width: 240px;
    top: 425px;
    text-align: center;
    color: var(--on-gold);
  }
  .holder__name {
    font-family: "Libre Baskerville", serif;
    font-weight: 700;
    font-size: 34px;
    line-height: 1.1;
  }
  .holder__role {
    font-family: "Nunito Sans", sans-serif;
    font-size: 31px;
    line-height: 1.3;
    letter-spacing: 1px;
  }
</style>
</head>
<body>
  <div class="card">
    <div class="card__pattern" role="img" aria-label="Faint decorative mandala pattern across the card background"></div>

    <svg class="card__art" width="1000" height="560" viewBox="0 0 1000 560" aria-hidden="true">
      <polyline points="40,513 40,38 961,38 961,358" fill="none" stroke="var(--gold)" stroke-width="6"/>
      <line x1="37" y1="513" x2="612" y2="513" stroke="var(--gold)" stroke-width="6"/>
      <path d="M612,560 C650,470 680,388 760,383 L1000,383 L1000,560 Z" fill="var(--gold-light)"/>
      <path d="M630,560 C668,472 696,392 776,383 L1000,383 L1000,560 Z" fill="var(--gold)"/>
    </svg>

    <div class="brand">
      <span class="brand__dot"></span>
      <span class="brand__name">Solara Oil &amp; Gas</span>
    </div>

    <ul class="contact">
      <li class="contact__item">
        <svg class="contact__icon" viewBox="0 0 24 24"><path d="M6.6 2.5 9.3 6 7.6 8.2c1.2 2.7 3.4 4.9 6.2 6.2l2.2-1.7 3.5 2.7-1.6 3.6C10.5 19 5 13.5 4 6.1z" fill="var(--ink)"/></svg>
        <span>(555) 014-2290</span>
      </li>
      <li class="contact__item">
        <svg class="contact__icon" viewBox="0 0 24 24"><rect x="2.5" y="5.5" width="19" height="13" fill="none" stroke="var(--ink)" stroke-width="1.6"/><polyline points="2.5,5.5 12,13 21.5,5.5" fill="none" stroke="var(--ink)" stroke-width="1.6"/><path d="M2.5 18.5 9.5 11.5M21.5 18.5 14.5 11.5" stroke="var(--ink)" stroke-width="1.6"/></svg>
        <span>info@solara-oilgas.com</span>
      </li>
      <li class="contact__item">
        <svg class="contact__icon" viewBox="0 0 24 24" fill="none" stroke="var(--ink)" stroke-width="1.6"><circle cx="12" cy="12" r="9"/><ellipse cx="12" cy="12" rx="4" ry="9"/><path d="M3 12h18M4.5 7.5h15M4.5 16.5h15"/></svg>
        <span>www.solara-oilgas.com</span>
      </li>
    </ul>

    <div class="holder">
      <div class="holder__name">Your Name</div>
      <div class="holder__role">OWNER</div>
    </div>
  </div>
</body>
</html>
```